Letterhead and Envelope Design for Investment Company

We need a letterhead and envelope design.
We are a family owned investment company doing direct investments into other family owned businesses.
I have attached all our current marketing material including our logo for reference.

Our under construction website can be found here:
https://owen-darby-qk7m.sitebrella.example/
password: Marrowdale

Target Market(s)

Bankers, business owners, financial partners

Industry/Entity Type

Investment

Colors

Designer to choose colors to be used in the design.

Requirements
Must have
• Logo, and company information

```html
<!DOCTYPE html>
<html lang="en">
<head>
<meta charset="utf-8">
<title>Marrowdale Holdings – Stationery</title>
<link rel="stylesheet" href="https://fonts.googleapis.com/css2?family=Cinzel:wght@500&family=Arimo:wght@400;500&family=Tinos&display=swap">
<style>
  :root {
    --backdrop: #7d7d7d;
    --paper: #ffffff;
    --ink: #1a1a1a;
    --black: #050505;
    --gold: #c99a2a;
    --gold-light: #e2b93b;
    --gold-dark: #a57a1c;
  }
  * { box-sizing: border-box; margin: 0; padding: 0; }
  html, body { width: 1200px; height: 900px; overflow: hidden; }
  body {
    position: relative;
    background: radial-gradient(ellipse at center, #8a8a8a 0%, var(--backdrop) 60%, #6c6c6c 100%);
    font-family: "Arimo", Arial, sans-serif;
    color: var(--ink);
  }
  .sheet { position: absolute; background: var(--paper); overflow: hidden; box-shadow: 0 1px 3px rgba(0,0,0,.25); }

  /* Wordmark */
  .wordmark { text-align: center; }
  .wordmark-name {
    font-family: "Cinzel", "Times New Roman", serif; font-weight: 500;
    color: var(--gold); letter-spacing: .04em; white-space: nowrap;
  }

  /* Letterhead */
  .letterhead { left: 57px; top: 102px; width: 533px; height: 692px; }
  .letterhead .wordmark { position: absolute; top: 82px; left: 0; width: 100%; }
  .letterhead .wordmark-name { font-size: 18px; }
  .recipient { position: absolute; left: 43px; top: 200px; font-size: 9px; line-height: 11px; }
  .recipient-name { font-size: 11px; font-weight: 500; margin-bottom: 5px; }
  .letter-content { position: absolute; left: 44px; top: 272px; width: 452px; }
  .letter-body { font-size: 9.4px; line-height: 15.6px; letter-spacing: -0.25px; }
  .letter-body p + p { margin-top: 15.6px; }
  .closing { font-size: 9.6px; line-height: 11px; }
  .signature {
    margin-top: 20px; width: 115px; height: 34px;
    background: linear-gradient(90deg, #ececec, #f6f6f6);
  }
  .signer { margin-top: 9px; font-size: 11px; font-weight: 500; }
  .letter-footer { position: absolute; left: 0; bottom: 0; width: 533px; height: 90px; }
  .letter-footer svg { position: absolute; inset: 0; }
  .footer-text {
    position: absolute; left: 0; top: 30px; width: 100%; text-align: center;
    font-family: "Tinos", "Times New Roman", serif; color: #fff;
  }
  .footer-company { font-family: "Cinzel", serif; font-size: 12px; letter-spacing: .06em; margin-bottom: 3px; }
  .footer-contact { font-size: 9.6px; line-height: 13px; }
  .footer-contact b { color: var(--gold-light); font-weight: 400; }

  /* Envelope front */
  .envelope-front { left: 670px; top: 103px; width: 472px; height: 235px; }
  .envelope-front .wordmark { position: absolute; left: 18px; top: 60px; text-align: left; }
  .envelope-front .wordmark-name { font-size: 13px; }
  .return-address {
    position: absolute; right: 23px; top: 23px; text-align: left; font-style: normal;
    font-family: "Tinos", serif; font-size: 8.4px; line-height: 11px;
  }
  .envelope-band { position: absolute; left: 0; bottom: 0; width: 472px; height: 60px; }
  .envelope-band svg { position: absolute; inset: 0; }
  .envelope-web {
    position: absolute; left: 0; top: 37px; width: 100%; text-align: center;
    font-family: "Tinos", serif; font-size: 8.6px; color: #fff;
  }

  /* Envelope back */
  .envelope-back { left: 670px; top: 370px; width: 472px; height: 235px; }
  .envelope-back svg.flap { position: absolute; left: 0; top: 0; }
  .envelope-back .wordmark { position: absolute; left: 0; top: 28px; width: 100%; }
  .envelope-back .wordmark-name { font-size: 12px; }
</style>
</head>
<body>

<section class="sheet letterhead" aria-label="Letterhead">
  <div class="wordmark"><span class="wordmark-name">Marrowdale Holdings Inc</span></div>

  <div class="recipient">
    <div class="recipient-name">JOHN SMITH</div>
    <div>Street Name,City Name.</div>
    <div>Zip Coad 0000</div>
  </div>

  <div class="letter-content">
    <div class="letter-body">
      <p>Lorem Ipsum is simply dummy text of the printing and typesetting industry. Lorem Ipsum has been the industry's standard dummy text ever since the 1500s, when an unknown printer took a galley of type and scrambled it to make a type specimen book. It has survived not only five centuries,but also the leap into electronic typesetting, remaining essentially unchanged. It was popularised in the 1960s with the release of Letraset sheets containing Lorem Ipsum passages, and more recently with desktop publishing software like Aldus PageMaker including versions of Lorem Ipsum.</p>
      <p>It is a long established fact that a reader will be distracted by the readable content of a page when looking at its layout. The point of using Lorem Ipsum is that it has a more-or-less normal distribution of letters, as opposed to using 'Content here, content here', making it look like readable English. Many desktop and publishing packages and web page editors now use Lorem Ipsum as their default model text, and a search for 'lorem ipsum' will uncover many web sites still in their infancy. Various versions have evolved over the years, sometimes by accident, sometimes on purpose (injected humour and the like).</p>
    </div>
    <div class="closing">Regards,</div>
    <div class="signature" role="img" aria-label="Handwritten signature of John Doe"></div>
    <div class="signer">John Doe</div>
  </div>

  <footer class="letter-footer">
    <svg width="533" height="90" viewBox="0 0 533 90" aria-hidden="true">
      <defs>
        <linearGradient id="goldBand" x1="0" x2="1" y1="0" y2="0">
          <stop offset="0" stop-color="var(--gold-dark)"/>
          <stop offset=".5" stop-color="var(--gold-light)"/>
          <stop offset="1" stop-color="var(--gold-dark)"/>
        </linearGradient>
      </defs>
      <path d="M0 44 Q266.5 -38 533 44 L533 90 L0 90 Z" fill="url(#goldBand)"/>
      <path d="M0 48 Q266.5 -24 533 48 L533 90 L0 90 Z" fill="var(--black)"/>
    </svg>
    <div class="footer-text">
      <div class="footer-company">Marrowdale Holdings, Inc.</div>
      <div class="footer-contact"><b>P:</b> 555 014 0426 | <b>E:</b> owen.darby@marrowdaleholdings.example | <b>W:</b> www.marrowdaleholdings.example</div>
      <div class="footer-contact">48 Linden Ave NE, Suite 210 Fernbrook, IA 50921</div>
    </div>
  </footer>
</section>

<section class="sheet envelope-front" aria-label="Envelope front">
  <div class="wordmark"><span class="wordmark-name">Marrowdale Holdings Inc</span></div>
  <address class="return-address">48 Linden Ave NE, Suite 210<br>Fernbrook, IA 50921</address>
  <div class="envelope-band">
    <svg width="472" height="60" viewBox="0 0 472 60" aria-hidden="true">
      <defs>
        <linearGradient id="goldBandEnv" x1="0" x2="1" y1="0" y2="0">
          <stop offset="0" stop-color="var(--gold-dark)"/>
          <stop offset=".5" stop-color="var(--gold-light)"/>
          <stop offset="1" stop-color="var(--gold-dark)"/>
        </linearGradient>
      </defs>
      <path d="M0 52 Q236 -26 472 52 L472 60 L0 60 Z" fill="url(#goldBandEnv)"/>
      <path d="M0 56 Q236 -16 472 56 L472 60 L0 60 Z" fill="var(--black)"/>
    </svg>
    <div class="envelope-web">www.marrowdaleholdings.example</div>
  </div>
</section>

<section class="sheet envelope-back" aria-label="Envelope back">
  <svg class="flap" width="472" height="70" viewBox="0 0 472 70" aria-hidden="true">
    <path d="M0 0 L472 0 L464 58 Q462 66 454 66 L18 66 Q10 66 9 58 Z" fill="var(--black)"/>
  </svg>
  <div class="wordmark"><span class="wordmark-name">Marrowdale</span></div>
</section>

</body>
</html>
```